Custom Cabinet Shop Needs a website design

Hi,
We need a website for a Custom Cabinet Shop and Cabinet parts manufacturing business.
The business has two sides to it. One side provides custom Kitchens, vanities, entertainment units, offices and what not to homeowners and contractors.
The 2nd side of the business provides built to order cabinet boxes and other parts required to put together a project to other cabinet shops, small contractors looking to install there own cabinets.
Website will need a Gallery to display work.
Color scheme to go well with logo.
current website is www.brindlewoodcustomcabinets.com
being changed to www.brindlewood.ca
Logo Included in attached files.
Tagline "Millwork with Flare"
Mission Statement "Our passion is to deliver inspired cabinetry solutions to suit all your needs, supported by our phenomenal star class customer service"
The website should convey quality and professionalism.
Thank you.
Homeowners/ Contractors
Entertainment
Coded - Design and coding required
1 page

```html
<!DOCTYPE html>
<html lang="en">
<head>
<meta charset="utf-8">
<title>Brindlewood Custom Cabinets</title>
<link href="https://fonts.googleapis.com/css2?family=Open+Sans:ital,wght@0,400;0,600;0,700;0,800;1,800&display=swap" rel="stylesheet">
<style>
  :root{
    --orange:#f05a22;
    --ink:#2b2b2b;
    --dark:#1f1f1f;
    --band:#333333;
    --page:#e9e9e9;
    --panel:#ffffff;
    --muted:#7a7a7a;
    --line:#cfcfcf;
  }
  *{margin:0;padding:0;box-sizing:border-box}
  html,body{width:851px;height:1200px;overflow:hidden}
  body{font-family:"Open Sans",Arial,sans-serif;color:var(--ink);background:var(--page);position:relative}

  .site-header{height:80px;background:#fff;position:relative}
  .brand{position:absolute;left:22px;top:22px;display:flex;align-items:center;gap:10px}
  .brand-mark{width:34px;height:34px;border-radius:50%;background:var(--dark)}
  .brand-name{font-weight:800;font-size:22px;letter-spacing:1px;color:var(--dark)}
  .main-nav{position:absolute;right:22px;top:22px;display:flex;gap:24px}
  .main-nav a{font-size:10px;font-weight:600;color:var(--ink);text-decoration:none;letter-spacing:.5px}
  .main-nav a.active{color:var(--orange)}
  .search{position:absolute;right:22px;top:46px;width:112px;height:18px;border:1px solid var(--line);background:#fff}
  .search svg{position:absolute;right:4px;top:3px}

  .hero{position:absolute;top:80px;left:0;width:851px;height:340px;
    background:linear-gradient(100deg,#1a1a1d 0%,#3a3a3f 30%,#6b5140 55%,#a37a55 75%,#3b2f28 100%)}
  .hero-caption{position:absolute;left:258px;top:70px;width:336px;height:150px;background:rgba(15,15,15,.78);text-align:center;padding-top:18px}
  .hero-title{font-weight:800;font-style:italic;font-size:28px;color:#fff;letter-spacing:.5px}
  .hero-title span{color:var(--orange)}
  .hero-text{font-size:9px;line-height:13px;color:#cfcfcf;width:250px;margin:10px auto 0}
  .hero-link{display:inline-block;margin-top:14px;font-size:8px;font-weight:700;color:#fff;letter-spacing:1px}
  .hero-arrow{position:absolute;top:160px;width:26px;height:26px;border-radius:50%;background:rgba(255,255,255,.85)}
  .hero-arrow.prev{left:22px}
  .hero-arrow.next{right:22px}
  .hero-arrow svg{position:absolute;left:8px;top:7px}

  .content{position:absolute;top:420px;left:70px;width:711px;height:716px;background:var(--panel)}
  .section-title{display:flex;align-items:center;justify-content:center;gap:14px;font-weight:700;font-size:17px;letter-spacing:1px}
  .section-title::before,.section-title::after{content:"";width:56px;height:1px;background:var(--ink)}
  .welcome{padding-top:30px}
  .mission{font-size:9px;line-height:14px;color:var(--muted);text-align:center;width:420px;margin:14px auto 0}

  .gallery-band{position:absolute;left:-44px;top:210px;width:799px;height:46px;background:var(--band);
    color:#fff;font-weight:700;font-size:17px;letter-spacing:1px;display:flex;align-items:center;justify-content:center;gap:14px}
  .gallery-band::before,.gallery-band::after{content:"";width:56px;height:1px;background:#fff}
  .gallery-grid{position:absolute;left:24px;top:275px;display:grid;grid-template-columns:repeat(4,156px);grid-auto-rows:128px;gap:14px}
  .tile{display:block}
  .t1{background:linear-gradient(135deg,#c9a27a,#7b5a3e)}
  .t2{background:linear-gradient(135deg,#3a2a22,#8a6a4a)}
  .t3{background:linear-gradient(135deg,#d8c8b4,#6a3a2e)}
  .t4{background:linear-gradient(135deg,#b98a5a,#4a3a30)}
  .t5{background:linear-gradient(135deg,#2a2a2e,#5a5a60)}
  .t6{background:linear-gradient(135deg,#c48a52,#5e4330)}
  .t7{background:linear-gradient(135deg,#1c1c1e,#7a6a58)}
  .t8{background:linear-gradient(135deg,#a88a6a,#3a3230)}

  .testimonials{position:absolute;left:0;top:578px;width:711px;text-align:center}
  .quote{font-size:9px;line-height:14px;color:var(--muted);width:380px;margin:16px auto 0}
  .quote-author{font-size:9px;color:var(--ink);margin-top:8px}
  .quote-mark{position:absolute;right:70px;top:56px}

  .site-footer{position:absolute;left:0;top:1136px;width:851px;height:64px;background:var(--dark)}
  .copyright{position:absolute;left:0;width:100%;top:26px;text-align:center;font-size:8px;color:#aaa}
  .social{position:absolute;right:36px;top:20px;display:flex;gap:8px}
  .social span{width:18px;height:18px;background:#8a8a8a}
</style>
</head>
<body>
  <header class="site-header">
    <div class="brand"><span class="brand-mark"></span><span class="brand-name">BRINDLEWOOD</span></div>
    <nav class="main-nav">
      <a class="active" href="#">HOME</a><a href="#">GALLERY</a><a href="#">SERVICES</a><a href="#">WARRANTY</a><a href="#">CONTACT</a>
    </nav>
    <div class="search">
      <svg width="11" height="11" viewBox="0 0 11 11"><circle cx="4.5" cy="4.5" r="3.3" fill="none" stroke="#f05a22" stroke-width="1.4"/><line x1="7" y1="7" x2="10" y2="10" stroke="#f05a22" stroke-width="1.6"/></svg>
    </div>
  </header>

  <section class="hero" role="img" aria-label="Photograph of a dark custom kitchen with wood floor, bar stools and wine storage">
    <div class="hero-caption">
      <h1 class="hero-title">MILLWORK WITH <span>FLARE</span></h1>
      <p class="hero-text">Crafted kitchens, vanities and built-ins made to order in our own shop, finished with care and installed with pride.</p>
      <span class="hero-link">READ MORE</span>
    </div>
    <span class="hero-arrow prev"><svg width="10" height="12" viewBox="0 0 10 12"><path d="M7 1 L2 6 L7 11" fill="none" stroke="#333" stroke-width="2"/></svg></span>
    <span class="hero-arrow next"><svg width="10" height="12" viewBox="0 0 10 12"><path d="M3 1 L8 6 L3 11" fill="none" stroke="#333" stroke-width="2"/></svg></span>
  </section>

  <main class="content">
    <section class="welcome">
      <h2 class="section-title">WELCOME</h2>
      <p class="mission">" Our passion is to deliver inspired cabinetry solutions to suit all your needs, supported by our phenomenal star class customer service "</p>
    </section>

    <h2 class="gallery-band">GALLERY</h2>
    <div class="gallery-grid">
      <span class="tile t1" role="img" aria-label="Kitchen with wood cabinets"></span>
      <span class="tile t2" role="img" aria-label="Dark kitchen with island"></span>
      <span class="tile t3" role="img" aria-label="Living room with red accent wall"></span>
      <span class="tile t4" role="img" aria-label="Room with fireplace and built-ins"></span>
      <span class="tile t5" role="img" aria-label="Dark cabinet wall"></span>
      <span class="tile t6" role="img" aria-label="Kitchen with wood floor"></span>
      <span class="tile t7" role="img" aria-label="Modern black cabinetry"></span>
      <span class="tile t8" role="img" aria-label="Open living area with furniture"></span>
    </div>

    <section class="testimonials">
      <h2 class="section-title">TESTIMONIALS</h2>
      <p class="quote">Working with the team was easy from the first drawing to the final install. Our new kitchen fits perfectly and the finish is flawless.</p>
      <p class="quote-author">Happy homeowner</p>
      <svg class="quote-mark" width="26" height="22" viewBox="0 0 26 22"><path d="M1 1h10v10l-4 10H3l3-9H1z M15 1h10v10l-4 10h-4l3-9h-5z" fill="#2b2b2b"/></svg>
    </section>
  </main>

  <footer class="site-footer">
    <p class="copyright">© 2015 Brindlewood. All rights are reserved.</p>
    <div class="social"><span></span><span></span><span></span><span></span></div>
  </footer>
</body>
</html>
```